Valve bag design

I need a valve bag for 25kg wall putty bag

Here are attached bags for reference

Most of the words or design you can copy from talvuno bag attached and company profile
Also I have attached our local product for reference

```html
<!DOCTYPE html>
<html lang="en">
<head>
<meta charset="utf-8">
<title>Crest Finish Wall Putty – 25kg Valve Bag</title>
<link rel="stylesheet" href="https://fonts.googleapis.com/css2?family=Archivo+Black&family=Montserrat:wght@800&family=Oswald:wght@300;400&family=Roboto+Condensed:wght@700&display=swap">
<style>
:root{
  --stage:#3a3b3f;
  --navy:#263e6c;
  --grey:#b0a79f;
  --white:#ffffff;
  --ink:#1d1d1f;
  --green:#7dcc2b;
}
*{box-sizing:border-box;margin:0;padding:0}
html,body{width:1200px;height:1200px;overflow:hidden;background:var(--stage)}
.canvas{position:relative;width:1200px;height:1200px}
.face-label{position:absolute;font-family:"Oswald",sans-serif;font-weight:400;color:var(--white);font-size:42px;line-height:1}
.bag{position:absolute;width:508px;height:762px;background:var(--white);overflow:hidden}
.bag--front{left:76px;top:146px}
.bag--back{left:618px;top:332px}
.band{position:absolute;left:0;width:100%;background:var(--navy)}
.strip{position:absolute;left:0;width:100%;background:var(--grey)}
.center{position:absolute;left:0;width:100%;text-align:center}
.brand-square{position:absolute;width:34px;height:34px;background:var(--navy);left:237px}
.brand-name{font-family:"Montserrat",sans-serif;font-weight:800;color:var(--navy);font-size:23px;letter-spacing:.5px;line-height:1}
.product-name{font-family:"Archivo Black",sans-serif;color:var(--navy);font-size:60px;line-height:1;letter-spacing:-1px;-webkit-text-stroke:1.5px var(--grey);paint-order:stroke fill}
.net-weight{position:absolute;left:401px;top:130px;width:90px;height:90px;border-radius:50%;background:var(--green);color:var(--white);font-family:"Archivo Black",sans-serif;text-align:center;line-height:1}
.net-weight small{display:block;font-size:14px;margin-top:22px}
.net-weight b{display:block;font-size:21px;font-weight:400}
.subtitle{font-family:"Roboto Condensed",sans-serif;font-weight:700;color:var(--ink);font-size:26px;line-height:1}
.tagline{font-family:"Montserrat",sans-serif;font-weight:800;color:var(--navy);font-size:18.5px;line-height:26px}
.features{position:absolute;left:110px;top:403px;width:281px;height:325px;background:var(--navy);border:5px solid var(--grey)}
.features h2{font-family:"Oswald",sans-serif;font-weight:400;color:var(--white);font-size:23px;position:absolute;left:17px;top:13px;letter-spacing:-.3px}
.feature{position:absolute;left:0;height:30px;width:100%}
.feature .tick{position:absolute;left:-18px;top:-1px;width:31px;height:31px}
.feature .icon{position:absolute;left:20px;top:0;width:32px;height:30px;border:2px solid var(--white)}
.feature span{position:absolute;left:63px;top:2px;font-family:"Oswald",sans-serif;font-weight:300;color:var(--white);font-size:16px;white-space:nowrap;letter-spacing:-.4px}
.info-box{position:absolute;border:1.5px solid var(--navy);font-family:"Oswald",sans-serif;color:var(--ink)}
.app-box{left:31px;top:309px;width:443px;height:178px;padding:8px 8px 0 18px}
.box-title{font-family:"Oswald",sans-serif;font-weight:400;font-size:12.5px;color:var(--ink);line-height:1.2}
.app-list{list-style:none;font-weight:300;font-size:7.6px;line-height:11.6px;margin-top:3px}
.app-list li{position:relative;padding-left:10px}
.app-list li.item::before{content:"";position:absolute;left:0;top:3px;width:5px;height:5px;background:var(--navy)}
.safety{position:absolute;left:31px;top:503px;width:455px;font-family:"Oswald",sans-serif;font-weight:300;font-size:8.4px;line-height:12.2px;color:var(--ink)}
.safety b{font-weight:400;font-size:11px}
.spec-box{left:27px;top:590px;width:231px;height:80px;padding:6px 8px}
.spec-table{border-collapse:collapse;font-weight:300;font-size:12px;line-height:17px;margin-top:1px}
.spec-table td{padding:0 8px 0 0;white-space:nowrap}
.distributor{position:absolute;left:288px;top:571px;width:195px;height:105px;background:var(--navy);color:var(--white);font-family:"Oswald",sans-serif;font-weight:300;padding:8px 12px;font-size:13px;line-height:17.5px}
.distributor .lead{font-size:14px;margin-bottom:4px}
</style>
</head>
<body>
<main class="canvas">

  <!-- FRONT FACE -->
  <section class="bag bag--front" aria-label="Front of bag">
    <div class="band" style="top:0;height:101px"></div>
    <div class="strip" style="top:101px;height:13px"></div>

    <div class="brand-square" style="top:150px"></div>
    <div class="center brand-name" style="top:206px">CREST FINISH</div>
    <div class="net-weight"><small>Net Wt.</small><b>25kg.</b></div>

    <h1 class="center product-name" style="top:237px">WALL PUTTY</h1>
    <p class="center subtitle" style="top:300px">White Cement Based Putty</p>
    <p class="center tagline" style="top:340px">Premium Wall putty to used for cement based<br>plaster and concrete surfaces before paint</p>

    <div class="strip" style="top:695px;height:12px"></div>
    <div class="band" style="top:707px;height:55px"></div>

    <div class="features">
      <h2>The Qualities &amp; Features</h2>
      <div class="feature" style="top:65px"><svg class="tick" viewBox="0 0 32 32"><circle cx="16" cy="16" r="16" fill="#7dcc2b"/><path d="M9 16l5 5 9-10" fill="none" stroke="#263e6c" stroke-width="3"/></svg><div class="icon"></div><span>Very smooth and glossy finish.</span></div>
      <div class="feature" style="top:99px"><svg class="tick" viewBox="0 0 32 32"><circle cx="16" cy="16" r="16" fill="#7dcc2b"/><path d="M9 16l5 5 9-10" fill="none" stroke="#263e6c" stroke-width="3"/></svg><div class="icon"></div><span>Suitable for all cement surfaces.</span></div>
      <div class="feature" style="top:134px"><svg class="tick" viewBox="0 0 32 32"><circle cx="16" cy="16" r="16" fill="#7dcc2b"/><path d="M9 16l5 5 9-10" fill="none" stroke="#263e6c" stroke-width="3"/></svg><div class="icon"></div><span>Suitable for Interior &amp; exterior.</span></div>
      <div class="feature" style="top:169px"><svg class="tick" viewBox="0 0 32 32"><circle cx="16" cy="16" r="16" fill="#7dcc2b"/><path d="M9 16l5 5 9-10" fill="none" stroke="#263e6c" stroke-width="3"/></svg><div class="icon"></div><span>Very high tensile adhesion.</span></div>
      <div class="feature" style="top:205px"><svg class="tick" viewBox="0 0 32 32"><circle cx="16" cy="16" r="16" fill="#7dcc2b"/><path d="M9 16l5 5 9-10" fill="none" stroke="#263e6c" stroke-width="3"/></svg><div class="icon"></div><span>Very low water absorption.</span></div>
      <div class="feature" style="top:240px"><svg class="tick" viewBox="0 0 32 32"><circle cx="16" cy="16" r="16" fill="#7dcc2b"/><path d="M9 16l5 5 9-10" fill="none" stroke="#263e6c" stroke-width="3"/></svg><div class="icon"></div><span>No water curing needed.</span></div>
      <div class="feature" style="top:277px"><svg class="tick" viewBox="0 0 32 32"><circle cx="16" cy="16" r="16" fill="#7dcc2b"/><path d="M9 16l5 5 9-10" fill="none" stroke="#263e6c" stroke-width="3"/></svg><div class="icon"></div><span>Very high coverage and easy to apply.</span></div>
    </div>
  </section>
  <p class="face-label" style="left:252px;top:952px">front</p>

  <!-- BACK FACE -->
  <p class="face-label" style="left:838px;top:258px">back</p>
  <section class="bag bag--back" aria-label="Back of bag">
    <div class="band" style="top:0;height:100px"></div>
    <div class="strip" style="top:100px;height:13px"></div>

    <div class="brand-square" style="top:146px"></div>
    <div class="center brand-name" style="top:203px">CREST FINISH</div>
    <h1 class="center product-name" style="top:236px">WALL PUTTY</h1>

    <div class="info-box app-box">
      <h3 class="box-title">APPLICATION RECOMMENDATIONS</h3>
      <ul class="app-list">
        <li class="item">Apply on cement / concrete cement plaster surfaces, wallboard and gypsum/plaster board.<br>25kg of Crest Finish Wall Putty added to approximately 8.5 - 10 liters of clean water, mixing may be done manually or by using a suitable electric mixer.</li>
        <li class="item">Prepared mortar is left to mature for 4 - 8 minutes and mixed again before use. The mortar must be used in 2 - 3 hours. Remove all dust, loose articles from the surface, oil, paint, curing agent, lime and silicones before application of Crest Finish Wall Putty.</li>
        <li class="item">Ensure that the surface is moisturized before the application, cracks and holes must be repaired with appropriate mortar.</li>
        <li class="item">Apply 1st coat of Crest Finish Wall Putty (1.5mm thickness) using a blade/spatula on the wall with a bottom to up configuration.</li>
        <li class="item">Apply 2nd coat of Crest Finish Wall Putty (1.0mm thickness) preferably after 4 hours during summers and after 12 hours during winters, second coat shall be applied horizontally to even out application marks of 1st coat, if any.</li>
        <li class="item">Consumption approximately 1kg/m2 (for 1mm thickness)</li>
        <li>Shelf life unopened bag can be stored in dry environment for up to 12 months, stacked maximum 12 packages on a place.</li>
      </ul>
    </div>

    <p class="safety"><b>Health and Safety:</b> Avoid contact with food, skin, eyes, and mouth during usage and strong use rubber gloves while mixing, take precautions to avoid dust infection while handling putty powdered by wearing noise mask, if swallowed by accident consult a doctor. Rinse with plenty of water in case of contact with skin.<br>KEEP OUT OF REACH OF CHILDREN</p>

    <div class="info-box spec-box">
      <h3 class="box-title">PRODUCT SPECIFICATIONS</h3>
      <table class="spec-table">
        <tr><td>Compressive Strength</td><td>28 day-14 N /mm</td></tr>
        <tr><td>Adhesion Strength</td><td>28 day-238 N /mm</td></tr>
        <tr><td>Water requirement by volume</td><td>38%</td></tr>
      </table>
    </div>

    <div class="distributor">
      <p class="lead">MARKETED AND DISTRIBUTED BY:</p>
      <p>HARLOW BUILDING LTD.</p>
      <p>Tel: +255700480219</p>
      <p>info@harlowbuilding.com</p>
      <p style="margin-top:-3px">harlowbuilding.com</p>
    </div>

    <div class="strip" style="top:698px;height:13px"></div>
    <div class="band" style="top:711px;height:51px"></div>
  </section>

</main>
</body>
</html>
```